Security Consulting firm needs an ad design

We need a 3.375” x 4.875” ad design for our core services. The ad should include the company logo and the content from the first half of the attached sample JPG (Without the sentence under the title but including the description for the Plan - Design - Deploy - Manage and the titles ) as well as the following corporate information:
www.harborlanepartners.us
82 Morrow Ave. Suite 615, Alder Brook, NJ 07690
PHONE 888-416-2057 / EMAIL info@harborlanepartners.us
The design should incorporate the same blue color that is in our logo and the font Raleway. Also - please use the same icons that are in the sample JPG - they can also be extracted from the attached indesign file.
The ad is to be publish in print and digital issue.
Please provide with all source files as well as a hi-res PDF using press quality or similar PDF settings.
- Raleway

```html
<!DOCTYPE html>
<html lang="en">
<head>
<meta charset="utf-8">
<title>Harbor Lane Partners – Creating Secure Environments</title>
<link rel="stylesheet" href="https://fonts.googleapis.com/css2?family=Raleway:wght@300;400;500;700;800;900&display=swap">
<style>
  :root {
    --navy: #141c2c;
    --navy-mid: #26334a;
    --photo-light: #4b5a70;
    --brand-blue: #3fa2e6;
    --service-blue: #2f72b8;
    --footer-blue: #2f78b9;
    --band: #e8eff6;
    --divider: #cfd8e2;
    --muted: #6b6f75;
    --white: #ffffff;
  }
  * { box-sizing: border-box; margin: 0; padding: 0; }
  html, body { width: 1200px; height: 831px; overflow: hidden; background: var(--white); }
  body { font-family: "Raleway", sans-serif; }

  .ad { position: relative; width: 1200px; height: 831px; overflow: hidden; }

  .hero {
    position: absolute; left: 0; top: 0; width: 1200px; height: 549px;
    background: var(--navy);
  }
  .hero-photo {
    position: absolute; inset: 0;
    background:
      radial-gradient(ellipse 420px 360px at 1000px 300px, var(--photo-light) 0%, rgba(75,90,112,0.35) 55%, rgba(20,28,44,0) 100%),
      linear-gradient(90deg, var(--navy) 0%, var(--navy) 40%, var(--navy-mid) 70%, #34425a 100%);
  }

  .brand {
    position: absolute; left: 80px; top: 70px;
    display: flex; align-items: center; gap: 16px;
  }
  .brand-dot { width: 54px; height: 54px; border-radius: 50%; background: var(--brand-blue); }
  .brand-name { color: var(--white); font-weight: 700; font-size: 44px; letter-spacing: -0.5px; }

  .headline { position: absolute; left: 80px; top: 172px; line-height: 1; }
  .headline-lead { display: block; color: var(--white); font-weight: 300; font-size: 84px; letter-spacing: -1px; }
  .headline-main { display: block; color: var(--brand-blue); font-weight: 800; font-size: 143px; letter-spacing: -1.5px; margin-top: -8px; }
  .headline-sub { display: block; color: var(--brand-blue); font-weight: 800; font-size: 71px; letter-spacing: 0; margin-top: 0; }

  .services {
    position: absolute; left: 0; top: 549px; width: 1200px; height: 165px;
    background: var(--band);
  }
  .service-divider { position: absolute; top: 29px; width: 2px; height: 115px; background: var(--divider); }

  .service { position: absolute; top: -53px; width: 290px; margin-left: -145px; text-align: center; }
  .service-badge {
    width: 102px; height: 102px; margin: 0 auto; border-radius: 50%;
    background: var(--white); box-shadow: 0 3px 6px rgba(0,0,0,0.22);
    display: flex; align-items: center; justify-content: center;
  }
  .service-badge svg { width: 50px; height: 50px; }
  .service-title { margin-top: 3px; color: var(--service-blue); font-weight: 800; font-size: 24px; }
  .service-text { margin-top: 0; color: var(--muted); font-weight: 400; font-size: 16.5px; line-height: 19px; }

  .contact {
    position: absolute; left: 0; top: 714px; width: 1200px; height: 117px;
    background: var(--footer-blue); color: var(--white);
  }
  .contact-divider { position: absolute; top: 26px; width: 2px; height: 72px; background: rgba(255,255,255,0.18); }
  .contact-phone { position: absolute; left: 52px; top: 24px; display: flex; align-items: center; gap: 10px; font-weight: 700; font-size: 37px; letter-spacing: 0.5px; }
  .contact-email { position: absolute; left: 52px; top: 68px; display: flex; align-items: center; gap: 10px; font-size: 23px; font-weight: 400; }
  .contact-address { position: absolute; left: 418px; top: 32px; display: flex; gap: 10px; }
  .contact-address p { font-size: 24px; font-weight: 400; line-height: 29px; }
  .contact-web { position: absolute; left: 798px; top: 45px; font-weight: 700; font-size: 23px; letter-spacing: 1.8px; }
</style>
</head>
<body>
<div class="ad">
  <section class="hero">
    <div class="hero-photo" role="img" aria-label="Photo of a security operator wearing a headset in a dim monitoring room"></div>
    <div class="brand">
      <span class="brand-dot"></span>
      <span class="brand-name">Harbor Lane Partners</span>
    </div>
    <h1 class="headline">
      <span class="headline-lead">CREATING</span>
      <span class="headline-main">SECURE</span>
      <span class="headline-sub">ENVIRONMENTS</span>
    </h1>
  </section>

  <section class="services">
    <span class="service-divider" style="left:346px"></span>
    <span class="service-divider" style="left:599px"></span>
    <span class="service-divider" style="left:890px"></span>

    <div class="service" style="left:201px">
      <div class="service-badge">
        <svg viewBox="0 0 50 50" fill="none" stroke="#2f72b8" stroke-width="3" stroke-linecap="round" stroke-linejoin="round">
          <rect x="9" y="7" width="32" height="40" rx="4"/>
          <rect x="18" y="3" width="14" height="8" rx="2" fill="#fff"/>
          <path d="M14 20l3 3 5-5M14 29l3 3 5-5M14 38l3 3 5-5"/>
          <path d="M27 21h9M27 30h9M27 39h9"/>
        </svg>
      </div>
      <h2 class="service-title">PLAN</h2>
      <p class="service-text">Security Assessment and<br>Planning Services</p>
    </div>

    <div class="service" style="left:473px">
      <div class="service-badge">
        <svg viewBox="0 0 50 50">
          <path fill="#2f72b8" d="M22 3h6l1 5 4 2 4-3 5 5-3 4 2 4 5 1v6l-5 1-2 4 3 4-5 5-4-3-4 2-1 5h-6l-1-5-4-2-4 3-5-5 3-4-2-4-5-1v-6l5-1 2-4-3-4 5-5 4 3 4-2z"/>
          <circle cx="25" cy="25" r="10" fill="#fff"/>
          <path stroke="#2f72b8" stroke-width="5" stroke-linecap="round" d="M21 21l20 20"/>
          <circle cx="20" cy="20" r="6" fill="none" stroke="#2f72b8" stroke-width="3"/>
        </svg>
      </div>
      <h2 class="service-title">DESIGN</h2>
      <p class="service-text">Security Design and<br>Engineering</p>
    </div>

    <div class="service" style="left:745px">
      <div class="service-badge">
        <svg viewBox="0 0 50 50" fill="#2f72b8">
          <path d="M44 6c-11 0-20 6-25 16l9 9c10-5 16-14 16-25z"/>
          <path d="M18 24l-9 1-4 6 9 1zM26 32l-1 9-6 4-1-9z"/>
          <path d="M13 35c-4 1-6 5-6 9 4 0 8-2 9-6z"/>
          <circle cx="33" cy="17" r="3.5" fill="#fff"/>
        </svg>
      </div>
      <h2 class="service-title">DEPLOY</h2>
      <p class="service-text">Procurement and Project<br>Management Services</p>
    </div>

    <div class="service" style="left:1034px">
      <div class="service-badge">
        <svg viewBox="0 0 50 50" fill="#2f72b8">
          <circle cx="25" cy="9" r="6"/>
          <path d="M15 26c0-7 4-10 10-10s10 3 10 10z"/>
          <path d="M7 31c8 4 28 4 36 0" fill="none" stroke="#2f72b8" stroke-width="3"/>
          <path d="M25 27v13" stroke="#2f72b8" stroke-width="3"/>
          <circle cx="6" cy="31" r="4"/><circle cx="44" cy="31" r="4"/><circle cx="25" cy="42" r="4"/>
        </svg>
      </div>
      <h2 class="service-title">MANAGE</h2>
      <p class="service-text">Comprehensive Security<br>Program Management</p>
    </div>
  </section>

  <footer class="contact">
    <span class="contact-divider" style="left:385px"></span>
    <span class="contact-divider" style="left:768px"></span>

    <div class="contact-phone">
      <svg width="26" height="26" viewBox="0 0 24 24" fill="#fff"><path d="M6.6 10.8a15.1 15.1 0 0 0 6.6 6.6l2.2-2.2c.3-.3.7-.4 1-.2 1.1.4 2.3.6 3.6.6.6 0 1 .4 1 1V20c0 .6-.4 1-1 1A17 17 0 0 1 3 4c0-.6.4-1 1-1h3.5c.6 0 1 .4 1 1 0 1.3.2 2.5.6 3.6.1.3 0 .7-.2 1z"/></svg>
      <span>888-416-2057</span>
    </div>
    <div class="contact-email">
      <svg width="26" height="18" viewBox="0 0 26 18" fill="#fff"><path d="M0 0h26v18H0z"/><path d="M1 1l12 9 12-9" fill="none" stroke="#2f78b9" stroke-width="2"/></svg>
      <span>info@harborlanepartners.us</span>
    </div>

    <div class="contact-address">
      <svg width="22" height="32" viewBox="0 0 22 32"><path fill="#fff" d="M11 0C5 0 0 5 0 11c0 8 11 21 11 21s11-13 11-21C22 5 17 0 11 0z"/><circle cx="11" cy="11" r="4.5" fill="#2f78b9"/></svg>
      <p>82 Morrow Ave. Suite 615,<br>Alder Brook, NJ 07690</p>
    </div>

    <div class="contact-web">www.harborlanepartners.us</div>
  </footer>
</div>
</body>
</html>
```